App Design for FlavorRoam

We need an app design for a new app called FlavorRoam, which is an app designed to inspire exploration through personalized recipe generation, local restaurant discoveries, and a vibrant community platform. It caters to food enthusiasts looking to explore global cuisines or find the best local dining spots, offering a premium experience with selected features available for free.

-------UPDATED-----
This app will be AI Driven and may not be heavily dependent on media (images,videos) at first, especially for the Recipe generator feature. Our goal is to still have attractive UI. The core functionalities we are looking are the following
1. Recipe Generator: Either user choose a specific cuisine(italian,spanish), or user inputs ingredients and get recipe, or get recipe for different occasions (xmas, thanksgiving ) and get a randomly get recipe to cook, plain simple. We expect the recipes to be displayed in clear and not too generic manner starting with ingredients and expected duration at top and then step by step guide. We also intend to enable premium users to have playful action button or icon to get unlimited recipes generated until they find what they like and also have save for later feature. These premium features should be disabled for free users and prompted to subscribe if they click them with nice popup
2. Restaurant Recommendation - will have selected pictures and will be based on inputs such as zip code and other filters such as cousine types. Premium users can filter by price range, get unlimited recommendation, see actual price range in the recommendation and can save for later where they can find it later. Free users cannot filter by price (disabled) and should see it hidden in the recommendation
3. Meal Planning - will include just simple and random meal plan with just one button or limited interaction for free, users need to subscribe to get features such as customized plan such as considering allergies or diet preferences. Premium users can also get a shopping checklist of ingredients for weekly meal preps and their step by step guide for each meal recipe.
2. Community Sharing: users can view posts and engage with community content
Updates

Hello Designers,

The initial price was not fair for the work. So I have increased it. There will also be $50-100 bonus for those who come up with great designs or for those who incorporate interesting stuff. Thank you! Much appreciated 🙏

Colors
0054AA
0677BA
7BADD7
CADEEF
E8F1F8
0094D4
00A9DD
6FCCEA
C7EBF8
E9F6FB
00AB8E
00BBA5
67D7C9
C6EFE9
E9F9F6
FFC000
F8CF3A
FAE287
FDF2CF
FEFAEE
F0912C
F2A743
F7CA91
FBE8D2
FDF5EE
EE7325
F08F49
F5BC92
FAE3D3
FDF4ED
A7469A
B969AE
D3A5CF
EDDBEB
F8F0F9
6B429C
8869AF
B7A5CE
E3DAEB
F3F0F8

```html
<!DOCTYPE html>
<html lang="en">
<head>
<meta charset="utf-8">
<title>FlavorRoam – App Screens</title>
<link href="https://fonts.googleapis.com/css2?family=Plus+Jakarta+Sans:wght@400;500;600;700;800&family=Libre+Baskerville&display=swap" rel="stylesheet">
<style>
:root{
  --board:#ececee;
  --bezel:#4a4b4e;
  --ink:#1d1d1f;
  --muted:#8a8d93;
  --label:#c3c5c9;
  --green:#2fc24b;
  --green-soft:#e5f7e9;
  --yellow:#f8cf3a;
  --yellow-soft:#fdf2cf;
  --surface:#f2f3f5;
  --line:#e3e5e8;
  --white:#fff;
  --dark:#2b2c2f;
}
*{box-sizing:border-box;margin:0;padding:0}
html,body{width:871px;height:1200px;overflow:hidden}
body{background:var(--board);font-family:"Plus Jakarta Sans",sans-serif;color:var(--ink);position:relative}
.section{position:absolute;font-size:8.5px;font-weight:700;color:var(--label)}
.caption{position:absolute;font-size:5.2px;font-weight:600}
.note{position:absolute;font-size:4px;color:var(--ink)}
.phone{position:absolute;width:79px;background:var(--bezel);border-radius:7px;padding:2.5px}
.scr{background:var(--white);border-radius:5px;height:100%;overflow:hidden;position:relative;display:flex;flex-direction:column;font-size:2.4px}
.scr.grey{background:var(--surface)}
.scr.night{background:#23252a;color:#fff}
.sb{display:flex;justify-content:space-between;padding:2px 3px 1px;font-size:2px;font-weight:700}
.sb i{display:inline-block;width:7px;height:1.6px;background:currentColor;border-radius:1px}
.hdr{display:flex;align-items:center;gap:2px;padding:1.5px 3px}
.avatar{width:7px;height:7px;border-radius:50%;background:linear-gradient(135deg,#d7b49d,#7b5442);flex:none}
.hdr b{display:block;font-size:2.3px}
.hdr small{display:block;font-size:1.6px;color:var(--muted)}
.hdr .tools{margin-left:auto;display:flex;gap:2px}
.hdr .tools span{width:3.5px;height:3.5px;border:.4px solid var(--muted);border-radius:1px}
.title{font-size:5.2px;font-weight:700;text-align:center;margin:3px 0 2px}
.serif{font-family:"Libre Baskerville",serif;font-weight:400}
.sub{font-size:2px;color:var(--muted);text-align:center;padding:0 5px;line-height:1.4}
.btn{display:flex;align-items:center;justify-content:center;height:6px;border-radius:1.5px;margin:1.5px 5px;font-size:2.3px;font-weight:600}
.btn.green{background:var(--green);color:#fff}
.btn.black{background:#111;color:#fff}
.btn.out{border:.4px solid var(--line);color:var(--ink)}
.btn.pill{border-radius:4px}
.btn.yellow{background:var(--yellow);color:#fff}
.field{height:5.5px;border:.4px solid var(--line);border-radius:1.2px;margin:1.3px 5px;display:flex;align-items:center;padding:0 2px;font-size:2px;color:var(--muted);background:#fafafa}
.img{display:block;background:linear-gradient(135deg,#6aa24a,#d9503a 55%,#f2c14b)}
.img.dark{background:linear-gradient(160deg,#3b2a22,#8a5a3a 50%,#1e1a18)}
.img.warm{background:linear-gradient(140deg,#e7733a,#c9402b 60%,#f4c35a)}
.img.room{background:linear-gradient(160deg,#2a2320,#a0673d 55%,#3a2c24)}
.card{background:#fff;border-radius:2px;margin:1.5px 3px;padding:2px}
.chips{display:flex;flex-wrap:wrap;gap:1.2px;padding:0 4px;justify-content:center}
.chip{border:.4px solid var(--line);border-radius:3px;padding:.8px 2.5px;font-size:1.9px;background:#fff}
.chip.on{border-color:var(--green);color:var(--green);background:var(--green-soft)}
.chip.fill{background:var(--green);color:#fff;border-color:var(--green)}
.chip.gold{background:var(--yellow);color:#fff;border-color:var(--yellow)}
.tabs{display:flex;justify-content:center;gap:3px;font-size:1.8px;color:var(--muted);margin:1px 0}
.tabs .on{background:var(--yellow);color:#fff;padding:.5px 2px;border-radius:2px}
.h6{font-size:2.3px;font-weight:700;padding:0 4px;margin:1.5px 0 .8px}
.p{font-size:1.8px;color:var(--muted);padding:0 4px;line-height:1.5}
.step{display:flex;gap:1.5px;padding:0 4px;margin-bottom:1.5px;font-size:1.6px;color:var(--muted);line-height:1.5}
.step:before{content:"";width:2px;height:2px;border-radius:50%;background:var(--green);flex:none;margin-top:.4px}
.row{display:flex;gap:2px;padding:0 4px;align-items:center}
.sub-banner{background:linear-gradient(90deg,var(--yellow-soft),#f6dfe4);margin:1.5px 4px;border-radius:1.5px;padding:1.5px 2px;font-size:1.9px;font-weight:600}
.list-item{display:flex;align-items:center;gap:2px;background:#fff;margin:1.3px 3px;padding:1.8px;border-radius:1.5px;font-size:2.1px}
.list-item .thumb{width:8px;height:7px;border-radius:1px}
.list-item .go{margin-left:auto;width:3px;height:3px;border-radius:50%;background:var(--line)}
.nav{position:absolute;bottom:0;left:0;right:0;height:10px;background:#f7f7f8;border-top:.3px solid var(--line);display:flex;justify-content:space-around;align-items:flex-end;padding-bottom:1px;font-size:1.3px;color:var(--muted)}
.nav span{display:flex;flex-direction:column;align-items:center;gap:.6px}
.nav span:before{content:"";width:3px;height:3px;border:.4px solid var(--muted);border-radius:.8px}
.nav .hub:before{width:7px;height:7px;border-radius:50%;background:var(--green);border:1px solid #fff;margin-top:-5px}
.days{display:flex;justify-content:center;gap:1px;margin:1px 0}
.days span{width:3.4px;height:3.4px;border-radius:50%;border:.4px solid var(--line);font-size:1.3px;display:flex;align-items:center;justify-content:center}
.days .on{background:var(--green);color:#fff;border-color:var(--green)}
.thanks{position:absolute;left:299px;top:1170px;font-size:34px;font-weight:800;letter-spacing:.5px;background:linear-gradient(#9a9ca1,rgba(236,236,238,0));-webkit-background-clip:text;background-clip:text;color:transparent}
.overlay{position:absolute;inset:0;background:rgba(30,30,32,.55)}
.popup{position:absolute;left:4px;right:4px;top:40px;background:#fff;border-radius:2px;padding:2px 0}
.mini-grid{display:grid;grid-template-columns:1fr 1fr;gap:2px;padding:0 3px}
.mini-grid .tile{background:#fff;border-radius:1.5px;padding:1px;font-size:1.7px}
.mini-grid .tile .img{height:12px;border-radius:1px}
</style>
</head>
<body>

<div class="section" style="left:36px;top:9px">Basic Screen</div>
<div class="section" style="left:36px;top:240px">Home Screen</div>
<div class="section" style="left:450px;top:245px">Recipe</div>
<div class="section" style="left:569px;top:245px">Cuisine</div>
<div class="section" style="left:33px;top:505px">Recipe Details</div>
<div class="section" style="left:249px;top:502px">Place to eat</div>

<!-- Row 1 captions -->
<div class="caption" style="left:38px;top:24px">00.Login screen</div>
<div class="caption" style="left:131px;top:24px">01.Login screen–1</div>
<div class="caption" style="left:223px;top:24px">02.Login screen–2</div>
<div class="caption" style="left:316px;top:24px">03.Register screen</div>
<div class="caption" style="left:409px;top:24px">04.Forgot password</div>
<div class="caption" style="left:499px;top:24px">05.Set new password</div>
<div class="caption" style="left:685px;top:28px">17.Meal Prep</div>

<!-- 00 -->
<div class="phone" style="left:39px;top:35px;height:169px"><div class="scr">
  <div class="sb"><span>5:50 am</span><i></i></div>
  <div class="img" role="img" aria-label="Fresh salad bowl with avocado and eggs" style="height:100px;background:linear-gradient(160deg,#f3f3f1,#8bbf5a 40%,#e6c46a 70%,#f1f1ef)"></div>
  <div class="sub" style="margin-top:5px">Hi, Please sign up to access your account</div>
  <div class="btn black">● Continue with Pearl</div>
  <div class="btn out">● Continue with Kestrel</div>
  <div class="btn green">Sign up with Email</div>
  <div class="sub" style="margin-top:2px">Already have an account? <b style="color:var(--ink)">Log in</b></div>
</div></div>

<!-- 01 -->
<div class="phone" style="left:131px;top:35px;height:169px"><div class="scr">
  <div class="sb"><span>5:50 am</span><i></i></div>
  <div class="img" role="img" aria-label="Illustration of a cooking pot with vegetables" style="width:40px;height:32px;margin:35px auto 6px;border-radius:50%;background:radial-gradient(#9aa4ad,#eef0f2 70%)"></div>
  <div class="sub">Hi, Please sign up to access your account</div>
  <div class="btn black">● Continue with Pearl</div>
  <div class="btn out">● Continue with Kestrel</div>
  <div class="btn green">Sign up with Email</div>
  <div class="sub" style="margin-top:2px">Already have an account? <b style="color:var(--ink)">Log in</b></div>
</div></div>

<!-- 02 -->
<div class="phone" style="left:224px;top:35px;height:163px"><div class="scr">
  <div class="sb"><span>5:50 am</span><i></i></div>
  <div class="img" role="img" aria-label="Illustration of a cooking pot with vegetables" style="width:34px;height:28px;margin:8px auto 4px;border-radius:50%;background:radial-gradient(#9aa4ad,#eef0f2 70%)"></div>
  <div class="title" style="font-size:4.2px;font-weight:500">Welcome to FlavorRoam</div>
  <div class="sub">Please enter the details below to continue</div>
  <div class="field" style="margin-top:3px">Email Address</div>
  <div class="field">Password</div>
  <div class="sub" style="text-align:right">Reset Password?</div>
  <div class="btn green">Login</div>
  <div class="sub">Don't have account? <span style="color:var(--green)">Create an Account</span></div>
  <div class="sub" style="margin:4px 0 2px">— or continue with —</div>
  <div class="row" style="justify-content:center"><div class="btn black pill" style="width:26px;margin:0">Pearl</div><div class="btn out pill" style="width:26px;margin:0">Kestrel</div></div>
</div></div>

<!-- 03 -->
<div class="phone" style="left:317px;top:35px;height:163px"><div class="scr">
  <div class="sb"><span>5:50 am</span><i></i></div>
  <div style="text-align:center;font-size:2.6px;font-weight:600;margin:2px 0">Register</div>
  <div class="title" style="font-size:3.6px;font-weight:500;margin-top:6px">Create a <b>New Account</b></div>
  <div class="sub">Enter your information's below</div>
  <div class="field" style="margin-top:3px">First Name</div>
  <div class="field">Last Name</div>
  <div class="field">Email Address</div>
  <div class="field">Password</div>
  <div class="field">Retype Password</div>
  <div class="btn green" style="margin-top:3px">Register</div>
  <div class="sub">Already have an account? <span style="color:var(--green)">Sign in</span></div>
</div></div>

<!-- 04 -->
<div class="phone" style="left:410px;top:35px;height:166px"><div class="scr">
  <div class="sb"><span>5:50 am</span><i></i></div>
  <div style="text-align:center;font-size:2.6px;font-weight:600;margin:2px 0">Forgot Password</div>
  <div class="title" style="font-size:3.6px;font-weight:500;margin-top:6px">Forgot your <b>Password?</b></div>
  <div class="sub">Enter the email address associated with your account</div>
  <div class="field" style="margin-top:3px">sam.lee@mailbox.test</div>
  <div class="btn green">Send Code</div>
</div></div>

<!-- 05 -->
<div class="phone" style="left:499px;top:35px;height:168px"><div class="scr">
  <div class="sb"><span>5:50 am</span><i></i></div>
  <div style="text-align:center;font-size:2.6px;font-weight:600;margin:2px 0">Reset Password</div>
  <div class="title" style="font-size:3.6px;font-weight:500;margin-top:6px">Set New <b>Password</b></div>
  <div class="sub">Please enter your new password and continue use the account</div>
  <div class="field" style="margin-top:3px">Password</div>
  <div class="field">Retype Password</div>
  <div class="btn green">Save</div>
  <div class="sub" style="color:var(--green);text-align:left">✓ Password Changed Successfully - <b style="color:var(--ink)">Home</b></div>
</div></div>

<!-- 17 Meal Prep -->
<div class="phone" style="left:681px;top:46px;height:386px"><div class="scr grey">
  <div class="img dark" role="img" aria-label="Dark table with prepared dishes" style="position:absolute;top:0;left:0;right:0;height:58px"></div>
  <div style="position:relative;color:#fff">
    <div class="sb"><span>5:50 am</span><i></i></div>
    <div class="hdr"><span class="avatar"></span><div><b>Hello Mira</b><small>Linden Square, Northvale</small></div></div>
    <div class="serif" style="text-align:center;font-size:4px;margin:8px 0 3px">Choose Meal Prep Duration</div>
    <div class="chips"><span class="chip" style="background:transparent;color:#fff">2 Days</span><span class="chip fill">3 Days</span><span class="chip" style="background:transparent;color:#fff">5 Days</span></div>
  </div>
  <div style="margin-top:14px;background:var(--green);color:#fff;font-size:2.2px;font-weight:600;padding:1.5px 4px;margin-left:2px;margin-right:2px">Day 1</div>
  <div style="background:#fff;margin:0 2px;padding-bottom:2px">
    <div class="tabs" style="justify-content:flex-start;padding:2px 4px"><span class="on">I have Ingredients</span><span>Generate Ingredients</span></div>
    <div class="field" style="margin:1px 4px">Tomato <span class="chip fill" style="margin-left:auto">ADD</span></div>
    <div class="row" style="margin:1.5px 0"><span class="chip">● Tomato</span><span class="chip">● Beef</span></div>
    <div class="h6">Gongura Chicken Curry Recipe</div>
    <div class="p">⏱ Eat Cooking Time : 20min</div>
    <div class="h6">Ingredients</div>
    <div class="row"><span class="chip">● Tomato</span><span class="chip">● Beef</span></div>
    <div class="h6">Spices</div>
    <div class="row"><span class="chip">● Cardamom</span><span class="chip">● Cinnamon</span></div>
    <div class="h6" style="margin-top:4px">Preparation</div>
    <div class="step">Start by washing the gongura leaves nicely. Transfer them to a pan and cook with green chillies, salt, and a bit of water for about 4 to 5 minutes.</div>
    <div class="step">Allow it to cool, then grind them to a smooth paste. Now, heat some oil in a kadhai set on a low-medium flame.</div>
    <div class="step">Add chopped onions and saute until golden brown in colour. Add haldi, coriander powder, jeera, and ginger-garlic paste and fry for a few seconds.</div>
    <div class="step">You can add some more water at this stage if needed. Once done, add the prepared gongura paste and let it simmer again for a minute or two.</div>
    <div class="btn yellow pill" style="margin:2px 4px">Save Ingredients</div>
  </div>
  <div class="card" style="margin:2px 2px 0;font-size:2.1px">Day 2</div>
  <div class="card" style="margin:1px 2px;font-size:2.1px">Day 3</div>
  <div class="card" style="margin:1px 2px;font-size:2.1px">Day 4</div>
  <div class="row" style="margin-top:3px"><div class="btn black pill" style="flex:1;margin:0;background:var(--dark)">Get Now</div><div class="btn green pill" style="flex:1;margin:0">Save For Later</div></div>
  <nav class="nav"><span>Restaurant</span><span class="hub">Recipe</span><span>Meal Plan</span><span>Community</span><span>Menu</span></nav>
</div></div>

<!-- Row 2 captions -->
<div class="caption" style="left:38px;top:274px">06.Home one</div>
<div class="caption" style="left:132px;top:274px">07.Home two</div>
<div class="caption" style="left:226px;top:274px">08.Home three</div>
<div class="caption" style="left:324px;top:274px">09.Home four</div>
<div class="caption" style="left:447px;top:270px">10.Recipe one</div>
<div class="caption" style="left:569px;top:267px">12.Cuisine one</div>

<!-- 06 -->
<div class="phone" style="left:39px;top:287px;height:169px"><div class="scr">
  <div class="sb"><span>5:50 am</span><i></i></div>
  <div class="hdr"><span class="avatar"></span><div><b>Hello Mira</b><small>Linden Square, Northvale</small></div></div>
  <div class="title" style="margin-top:28px;font-weight:600;font-size:4.4px">Hi User,</div>
  <div class="sub" style="color:var(--ink);font-size:3px">What's What'd you like today?</div>
  <div class="btn green" style="height:8px;margin-top:3px">Get a Recipe</div>
  <div class="sub">Discover recipes based on ingredients, cuisines or generate a random recipe</div>
  <div class="row" style="justify-content:space-around;margin-top:5px;font-size:1.8px;color:var(--green)"><span>◎ Eat Out</span><span>◎ Plan a Meal</span><span>◎ Community</span></div>
</div></div>

<!-- 07 -->
<div class="phone" style="left:132px;top:287px;height:169px"><div class="scr">
  <div class="sb"><span>5:50 am</span><i></i></div>
  <div class="hdr"><span class="avatar"></span><div><b>Hello Mira</b><small>Linden Square, Northvale</small></div></div>
  <div class="title" style="margin-top:28px;font-weight:600;font-size:4.4px">Hi User,</div>
  <div class="sub" style="color:var(--ink);font-size:3px">What's What'd you like today?</div>
  <div class="btn green" style="height:8px;margin-top:3px">Get a Recipe</div>
  <div class="sub">Discover recipes based on ingredients, cuisines or generate a random recipe</div>
  <div class="row" style="justify-content:space-around;margin-top:5px;font-size:1.8px;color:var(--green)"><span class="card" style="border:.4px solid var(--line)">Eat Out</span><span class="card" style="border:.4px solid var(--line)">Plan a Meal</span><span class="card" style="border:.4px solid var(--line)">Community</span></div>
</div></div>

<!-- 08 -->
<div class="phone" style="left:226px;top:287px;height:172px"><div class="scr">
  <div class="sb"><span>5:50 am</span><i></i></div>
  <div class="hdr"><span class="avatar"></span><div><b>Hello Mira</b><small>Linden Square, Northvale</small></div></div>
  <div class="img warm" role="img" aria-label="Bowl of tomato curry with lime and herbs" style="height:70px;margin:2px 0"></div>
  <div class="title" style="font-weight:600;font-size:4.4px;margin-top:4px">Hi User,</div>
  <div class="sub" style="color:var(--ink);font-size:3px">What's What'd you like today?</div>
  <div class="btn green pill" style="height:8px;margin-top:3px">Get a Recipe</div>
  <div class="sub">Discover recipes based on ingredients, cuisines or generate a random recipe</div>
  <div class="row" style="justify-content:space-around;margin-top:4px;font-size:1.8px;color:var(--green)"><span>◯ Eat Out</span><span>◯ Plan a Meal</span><span>◯ Community</span></div>
</div></div>

<!-- 09 -->
<div class="phone" style="left:324px;top:287px;height:169px"><div class="scr night">
  <div class="img dark" role="img" aria-label="Overhead view of assorted dishes on a dark table" style="position:absolute;inset:0 0 50px 0;background:linear-gradient(150deg,#2c2a26,#b8642f 35%,#3b5a2a 60%,#222)"></div>
  <div class="sb" style="position:relative"><span>5:50 am</span><i></i></div>
  <div style="position:relative;margin-top:92px">
    <div class="hdr"><span class="avatar"></span><div><b>Hello Mira</b><small style="color:#ccc">Linden Square, Northvale</small></div></div>
    <div class="btn green pill" style="height:8px">Get a Recipe</div>
    <div class="sub" style="color:#bbb">Discover recipes based on ingredients, cuisines or generate a random recipe</div>
    <div class="row" style="justify-content:space-around;margin-top:4px;font-size:1.8px;color:var(--green)"><span>◯ Eat Out</span><span>◯ Plan a Meal</span><span>◯ Community</span></div>
  </div>
</div></div>

<!-- 10 Recipe one -->
<div class="phone" style="left:448px;top:281px;height:186px"><div class="scr grey">
  <div class="sb"><span>5:50 am</span><i></i></div>
  <div class="hdr"><span class="avatar"></span><div><b>Hello Mira</b><small>Linden Square, Northvale</small></div><div class="tools"><span></span><span></span></div></div>
  <div class="title">Recipes</div>
  <div class="btn green pill" style="height:7px;justify-content:flex-start;padding-left:4px">Surprise Me</div>
  <div class="card" style="margin-top:3px">
    <div style="text-align:center;font-size:2.2px;font-weight:600;margin:1px 0">Customise Your Recipe</div>
    <div class="tabs"><span class="on">Add Ingredients</span><span>Cuisine</span><span>Occasion</span></div>
    <div class="field" style="margin:2px 1px">Tomato <span class="chip fill" style="margin-left:auto">ADD</span></div>
    <div class="row" style="padding:0 1px;margin:1.5px 0"><span class="chip">● Tomato</span><span class="chip">● Beef</span></div>
    <div class="row" style="padding:0 1px"><span class="chip">● Onion</span><span class="chip">● Avocado</span></div>
    <div class="sub-banner" style="margin:2px 1px">Subscribe to<br><span style="font-weight:400;color:var(--muted)">Add Maximum Cooking Time</span></div>
    <div class="btn green pill" style="margin:3px 1px 1px">Get Your Recipe</div>
  </div>
  <nav class="nav"><span>Restaurant</span><span class="hub">Recipe</span><span>Meal Plan</span><span>Community</span><span>Menu</span></nav>
</div></div>

<!-- 12 Cuisine one -->
<div class="phone" style="left:570px;top:282px;height:209px"><div class="scr grey">
  <div class="sb"><span>5:50 am</span><i></i></div>
  <div class="hdr"><span class="avatar"></span><div><b>Hello Mira</b><small>Linden Square, Northvale</small></div><div class="tools"><span></span><span></span></div></div>
  <div class="title">Recipes</div>
  <div class="btn green pill" style="height:7px;justify-content:flex-start;padding-left:4px">Surprise Me</div>
  <div class="card" style="margin-top:3px">
    <div style="text-align:center;font-size:2.2px;font-weight:600;margin:1px 0">Customise Your Recipe</div>
    <div class="tabs"><span>Add Ingredients</span><span class="on">Cuisine</span><span>Occasion</span></div>
    <div class="row" style="padding:0 1px;margin:2px 0"><span style="font-size:1.9px">Choose Your Cuisine</span><span class="sub-banner" style="margin:0">Subscribe to</span></div>
    <div class="chips" style="margin-top:2px"><span class="chip on">American</span><span class="chip on">Indian</span><span class="chip">Mexican</span><span class="chip">Japanese</span><span class="chip">Chinese</span><span class="chip">Italian</span><span class="chip">African</span><span class="chip">French</span><span class="chip">Spanish</span></div>
  </div>
  <div class="card">
    <div class="field" style="margin:1px">Tomato <span class="chip fill" style="margin-left:auto">ADD</span></div>
    <div class="row" style="padding:0 1px;margin:1.5px 0"><span class="chip">● Tomato</span><span class="chip">● Beef</span></div>
    <div class="btn green pill" style="margin:2px 1px">Get Your Recipe</div>
  </div>
  <nav class="nav"><span>Restaurant</span><span class="hub">Recipe</span><span>Meal Plan</span><span>Community</span><span>Menu</span></nav>
</div></div>

<!-- Row 3 captions -->
<div class="caption" style="left:33px;top:526px">13.Recipe Details</div>
<div class="caption" style="left:143px;top:526px">14.Cuisine Popup</div>
<div class="caption" style="left:249px;top:526px">15.Place to eat</div>
<div class="caption" style="left:347px;top:526px">16.Place to eat – subscription</div>
<div class="caption" style="left:512px;top:547px">24.Community</div>
<div class="caption" style="left:611px;top:541px">25.Recipe Results</div>
<div class="caption" style="left:611px;top:552px">(if we have two more recipes)</div>

<!-- 13 Recipe Details -->
<div class="phone" style="left:24px;top:549px;height:304px"><div class="scr grey">
  <div class="sb"><span>5:50 am</span><i></i></div>
  <div class="hdr"><span class="avatar"></span><div><b>Hello Mira</b><small>Linden Square, Northvale</small></div><div class="tools"><span></span><span></span></div></div>
  <div class="title">Recipe Details</div>
  <div class="btn green" style="height:7px;justify-content:flex-start;padding-left:4px;margin:1px 3px">Surprise Me</div>
  <div class="card" style="margin-top:3px">
    <div style="font-size:2.2px;font-weight:600">Customise Your Recipe</div>
    <div class="p" style="padding:0;margin-top:2px">Choose Cuisine</div>
    <div class="row" style="padding:0;margin-top:1px"><span class="chip">American</span><span class="chip">Indian</span><span class="chip fill">Load More</span></div>
  </div>
  <div class="card">
    <div class="h6" style="padding:0">Gongura Chicken Curry Recipe</div>
    <div class="p" style="padding:0">⏱ Eat Cooking Time : 20min</div>
    <div class="h6" style="padding:0;margin-top:3px">Ingredients</div>
    <div class="row" style="padding:0"><span class="chip">● Tomato</span><span class="chip">● Beef</span></div>
    <div class="h6" style="padding:0;margin-top:3px">Spices</div>
    <div class="row" style="padding:0"><span class="chip">● Cardamom</span><span class="chip">● Cinnamon</span></div>
    <div class="btn green pill" style="margin:3px 0 1px">Save Ingredients</div>
  </div>
  <div class="card">
    <div class="h6" style="padding:0;margin-bottom:2px">Preparation</div>
    <div class="step" style="padding:0">Start by washing the gongura leaves nicely. Transfer them to a pan and cook with green chillies, salt, and a bit of water for about 4 to 5 minutes.</div>
    <div class="step" style="padding:0">Allow it to cool, then grind them to a smooth paste. Now, heat some oil in a kadhai set on a low-medium flame.</div>
    <div class="step" style="padding:0">Add chopped onions and saute until golden brown in colour. Add haldi, coriander powder, jeera, and ginger-garlic paste and fry for a few seconds.</div>
    <div class="step" style="padding:0">You can add some more water at this stage if needed. Once done, add the prepared gongura paste and let it simmer again for a minute or two.</div>
    <div class="row" style="padding:0;margin-top:2px"><div class="btn pill" style="flex:1;margin:0;background:var(--dark);color:#fff">Get Now</div><div class="btn green pill" style="flex:1;margin:0">Save For Later</div></div>
  </div>
</div></div>

<!-- 14 Cuisine Popup -->
<div class="phone" style="left:141px;top:541px;height:163px"><div class="scr grey">
  <div class="sb"><span>5:50 am</span><i></i></div>
  <div class="hdr"><span class="avatar"></span><div><b>Hello Mira</b><small>Linden Square, Northvale</small></div></div>
  <div class="title">Recipe Details</div>
  <div class="btn green" style="height:7px;justify-content:flex-start;padding-left:4px;margin:1px 3px">Surprise Me</div>
  <div class="h6" style="margin-top:76px">Spices</div>
  <div class="row"><span class="chip">Cardamom</span><span class="chip">Cinnamon</span></div>
  <div class="h6" style="margin-top:4px">Preparation</div>
  <div class="overlay"></div>
  <div class="popup" style="top:27px">
    <div style="font-size:2.3px;font-weight:600;padding:0 3px;margin-bottom:3px">⊕ Add Your Cuisine</div>
    <div class="chips"><span class="chip on">American</span><span class="chip on">Indian</span><span class="chip">Mexican</span><span class="chip">Japanese</span><span class="chip">Chinese</span><span class="chip">Italian</span><span class="chip">African</span><span class="chip">French</span><span class="chip">Spanish</span></div>
    <div class="btn green" style="margin:3px 3px 1px">Load Cuisine</div>
  </div>
</div></div>

<!-- 15 Place to eat -->
<div class="phone" style="left:249px;top:541px;height:249px"><div class="scr grey">
  <div class="img room" role="img" aria-label="Dim restaurant interior" style="position:absolute;top:0;left:0;right:0;height:66px;background:linear-gradient(160deg,#3a3330,#2a2624)"></div>
  <div style="position:relative;color:#fff">
    <div class="sb"><span>5:50 am</span><i></i></div>
    <div class="hdr"><span class="avatar"></span><div><b>Hello Mira</b><small style="color:#ccc">Linden Square, Northvale</small></div><div class="tools"><span style="border-color:#fff"></span><span style="border-color:#fff"></span></div></div>
    <div class="serif" style="text-align:center;font-size:3.8px;margin:5px 0 2px">Lets get you a place to eat</div>
    <div class="field" style="margin:0 18px;background:#fff;color:var(--ink)">Zip Code &nbsp;123456</div>
    <div class="row" style="font-size:1.7px;margin-top:5px;justify-content:space-between"><span>Choose Meal Type</span><span>Distance &nbsp; Price Range</span></div>
    <div class="row" style="justify-content:space-between;margin-top:1px"><span><span class="chip gold">Cuisine</span> <span class="chip" style="background:transparent;color:#ccc">Occasion</span></span><span style="display:flex;gap:1px"><span class="chip">5M</span><span class="chip">50</span><span class="chip">2500</span></span></div>
  </div>
  <div class="sub" style="color:var(--ink);margin-top:9px">Here's a good restaurant based on your preferences. A very nice food here.</div>
  <div class="card" style="margin:3px 5px">
    <div class="img room" role="img" aria-label="Restaurant dining room with warm lighting" style="height:60px;border-radius:1px"></div>
    <div class="serif" style="text-align:center;font-size:2.4px;margin-top:2px">The Copper Ladle</div>
    <div class="p" style="text-align:center">⌖ 48 Orchard Lane, Northvale 20418</div>
  </div>
  <div class="row" style="justify-content:center;margin-top:3px"><div class="btn yellow pill" style="width:27px;margin:0">Premium</div><div class="btn green pill" style="width:27px;margin:0">Save for Later</div></div>
  <nav class="nav"><span>Restaurant</span><span class="hub">Recipe</span><span>Meal Plan</span><span>Community</span><span>Menu</span></nav>
</div></div>

<!-- 16 Place to eat – subscription -->
<div class="phone" style="left:348px;top:541px;height:243px"><div class="scr grey">
  <div class="img room" role="img" aria-label="Dim restaurant interior" style="position:absolute;top:0;left:0;right:0;height:66px;background:linear-gradient(160deg,#3a3330,#2a2624)"></div>
  <div style="position:relative;color:#fff">
    <div class="sb"><span>5:50 am</span><i></i></div>
    <div class="hdr"><span class="avatar"></span><div><b>Hello Mira</b><small style="color:#ccc">Linden Square, Northvale</small></div><div class="tools"><span style="border-color:#fff"></span><span style="border-color:#fff"></span></div></div>
    <div class="serif" style="text-align:center;font-size:3.8px;margin:5px 0 2px">Lets get you a place to eat</div>
    <div class="field" style="margin:0 18px;background:#fff;color:var(--ink)">Zip Code &nbsp;123456</div>
    <div style="text-align:right;padding-right:4px;margin-top:2px"><span class="chip" style="background:#eee;color:var(--ink)">● Subscribe to Add</span></div>
    <div class="row" style="font-size:1.7px;margin-top:1px;justify-content:space-between"><span>Choose Meal Type</span><span>Distance &nbsp; Price Range</span></div>
    <div class="row" style="justify-content:space-between;margin-top:1px"><span><span class="chip gold">Cuisine</span> <span class="chip" style="background:transparent;color:#ccc">Occasion</span></span><span style="display:flex;gap:1px"><span class="chip">5M</span><span class="chip">50</span><span class="chip">2500</span></span></div>
  </div>
  <div class="sub" style="color:var(--ink);margin-top:8px">Here's a good restaurant based on your preferences. A very nice food here.</div>
  <div class="card" style="margin:3px 5px">
    <div class="img room" role="img" aria-label="Restaurant dining room with warm lighting" style="height:60px;border-radius:1px"></div>
    <div class="serif" style="text-align:center;font-size:2.4px;margin-top:2px">The Copper Ladle</div>
    <div class="p" style="text-align:center">⌖ 48 Orchard Lane, Northvale 20418</div>
  </div>
  <div class="row" style="justify-content:center;margin-top:3px"><div class="btn yellow pill" style="width:27px;margin:0">Premium</div><div class="btn green pill" style="width:27px;margin:0">Save for Later</div></div>
  <nav class="nav"><span>Restaurant</span><span class="hub">Recipe</span><span>Meal Plan</span><span>Community</span><span>Menu</span></nav>
</div></div>

<!-- 24 Community -->
<div class="phone" style="left:513px;top:566px;height:187px"><div class="scr grey">
  <div class="sb"><span>5:50 am</span><i></i></div>
  <div class="hdr"><span class="avatar"></span><div><b>Hello Mira</b><small>Linden Square, Northvale</small></div><div class="tools"><span></span><span></span></div></div>
  <div class="card">
    <div class="img warm" role="img" aria-label="Plate of burritos in sauce" style="height:30px;border-radius:1px"></div>
    <div style="font-size:2.3px;margin-top:1.5px">Avocado sauce burritos</div>
    <div class="p" style="padding:0">Friday, 27 June 2024 · 8.30 am</div>
    <div class="row" style="padding:0;margin-top:1px"><span class="chip on">35 Comments</span><span class="chip" style="color:#e24">♥ 100</span></div>
  </div>
  <div class="card">
    <div class="img" role="img" aria-label="Salad with crispy tofu cubes" style="height:30px;border-radius:1px;background:linear-gradient(135deg,#f1e6d6,#b6532c 40%,#6fa83c 70%,#f0c742)"></div>
    <div style="font-size:2.3px;margin-top:1.5px">Avocado sauce burritos</div>
    <div class="p" style="padding:0">Friday, 27 June 2024 · 8.30 am</div>
    <div class="row" style="padding:0;margin-top:1px"><span class="chip on">35 Comments</span><span class="chip" style="color:#e24">♥ 100</span></div>
  </div>
  <div class="card"><div class="img" role="img" aria-label="Colourful bowls of food" style="height:14px"></div></div>
  <nav class="nav"><span>Restaurant</span><span class="hub">Recipe</span><span>Meal Plan</span><span>Community</span><span>Menu</span></nav>
</div></div>

<!-- 25 Recipe Results -->
<div class="phone" style="left:609px;top:566px;height:200px"><div class="scr grey">
  <div class="sb"><span>5:50 am</span><i></i></div>
  <div class="hdr"><span class="avatar"></span><div><b>Hello Mira</b><small>Linden Square, Northvale</small></div><div class="tools"><span></span><span></span></div></div>
  <div class="title">Recipes Results</div>
  <div class="mini-grid">
    <div class="tile"><div class="img warm" role="img" aria-label="Asparagus frittata in a bowl"></div><div>Asparagus Frittata</div><div style="color:var(--muted)">⏱ 20min</div><span class="chip fill" style="font-size:1.4px">Save Ingredients</span></div>
    <div class="tile"><div class="img" role="img" aria-label="Tomato and vegetable dish"></div><div>Asparagus Frittata</div><div style="color:var(--muted)">⏱ 20min</div><span class="chip fill" style="font-size:1.4px">Save Ingredients</span></div>
    <div class="tile"><div class="img warm" role="img" aria-label="Curry in a bowl"></div><div>Asparagus Frittata</div><div style="color:var(--muted)">⏱ 20min</div><span class="chip fill" style="font-size:1.4px">Save Ingredients</span></div>
  </div>
  <nav class="nav"><span>Restaurant</span><span class="hub">Recipe</span><span>Meal Plan</span><span>Community</span><span>Menu</span></nav>
</div></div>

<!-- Row 4 captions -->
<div class="caption" style="left:34px;top:871px">23.Saved items</div>
<div class="caption" style="left:123px;top:874px">18.Saved Restaurant</div>
<div class="caption" style="left:228px;top:874px">19.Saved Recipes</div>
<div class="caption" style="left:318px;top:874px">20.Shop Ingredient</div>
<div class="caption" style="left:415px;top:874px">21.Meal Plan</div>
<div class="caption" style="left:507px;top:912px">22.Meal Plan – Subscription</div>
<div class="caption" style="left:742px;top:896px">Menu</div>

<!-- 23 Saved items -->
<div class="phone" style="left:30px;top:890px;height:169px"><div class="scr grey">
  <div class="sb"><span>5:50 am</span><i></i></div>
  <div class="hdr"><span class="avatar"></span><div><b>Hello Mira</b><small>Linden Square, Northvale</small></div><div class="tools"><span></span><span></span></div></div>
  <div class="title">Saved Items</div>
  <div class="list-item"><span class="thumb img warm" role="img" aria-label="Recipe dish"></span><div>Saved Recipes<div style="font-size:1.6px;color:var(--muted)">15 Recipes</div></div><span class="go"></span></div>
  <div class="list-item"><span class="thumb img room" role="img" aria-label="Restaurant table"></span><div>Saved Restaurant<div style="font-size:1.6px;color:var(--muted)">10 Restaurant</div></div><span class="go"></span></div>
  <div class="list-item"><span class="thumb img dark" role="img" aria-label="Meal prep containers"></span><div>Meal Preps<div style="font-size:1.6px;color:var(--muted)">5 Meals</div></div><span class="go"></span></div>
  <nav class="nav"><span>Restaurant</span><span class="hub">Recipe</span><span>Meal Plan</span><span>Community</span><span>Menu</span></nav>
</div></div>

<!-- 18 Saved Restaurant -->
<div class="phone" style="left:124px;top:887px;height:222px"><div class="scr grey">
  <div class="sb"><span>5:50 am</span><i></i></div>
  <div class="hdr"><span class="avatar"></span><div><b>Hello Mira</b><small>Linden Square, Northvale</small></div><div class="tools"><span></span><span></span></div></div>
  <div class="title">Saved Restaurant</div>
  <div class="card" style="padding:0 0 1.5px"><div class="img room" role="img" aria-label="Restaurant terrace with fire pit" style="height:25px"></div><div style="font-size:2.1px;padding:1px 2px">The Harbor Table</div><div class="p" style="padding:0 2px">Slow-cooked beef chili with bacon, tomato and herbs.</div><div class="p" style="padding:0 2px">★ 4.8 (233 Ratings) · 5.5mi · <span style="color:var(--green)">Opened</span></div></div>
  <div class="card" style="padding:0 0 1.5px"><div class="img room" role="img" aria-label="Bright dining hall" style="height:25px;background:linear-gradient(160deg,#c7b49c,#6a4c35)"></div><div style="font-size:2.1px;padding:1px 2px">The Harbor Table</div><div class="p" style="padding:0 2px">Slow-cooked beef chili with bacon, tomato and herbs.</div><div class="p" style="padding:0 2px">★ 4.8 (233 Ratings) · 5.5mi · <span style="color:var(--green)">Opened</span></div></div>
  <div class="card" style="padding:0 0 1.5px"><div class="img room" role="img" aria-label="Red-lit hotel dining room" style="height:25px;background:linear-gradient(160deg,#5a1d16,#b04a2c)"></div><div style="font-size:2.1px;padding:1px 2px">Willow Court Hotel</div><div class="p" style="padding:0 2px">Slow-cooked beef chili with bacon, tomato and herbs.</div></div>
  <nav class="nav"><span>Restaurant</span><span class="hub">Recipe</span><span>Meal Plan</span><span>Community</span><span>Menu</span></nav>
</div></div>

<!-- 19 Saved Recipes -->
<div class="phone" style="left:225px;top:887px;height:202px"><div class="scr grey">
  <div class="sb"><span>5:50 am</span><i></i></div>
  <div class="hdr"><span class="avatar"></span><div><b>Hello Mira</b><small>Linden Square, Northvale</small></div><div class="tools"><span></span><span></span></div></div>
  <div class="title">Saved Recipes</div>
  <div class="mini-grid">
    <div class="tile"><div class="img warm" role="img" aria-label="Frittata dish"></div><div>Asparagus Frittata</div><div style="color:var(--muted)">⏱ 20min</div></div>
    <div class="tile"><div class="img" role="img" aria-label="Baked salmon dish"></div><div>Backed Salmon</div><div style="color:var(--muted)">⏱ 20min</div></div>
    <div class="tile"><div class="img warm" role="img" aria-label="Roasted eggplant salad"></div><div>Roasted eggplant salad</div><div style="color:var(--muted)">⏱ 20min</div></div>
    <div class="tile"><div class="img" role="img" aria-label="Pozole bowl"></div><div>Appetizing pozole bowl</div><div style="color:var(--muted)">⏱ 20min</div></div>
    <div class="tile"><div class="img warm" role="img" aria-label="Frittata dish"></div><div>Asparagus Frittata</div><div style="color:var(--muted)">⏱ 20min</div></div>
    <div class="tile"><div class="img" role="img" aria-label="Baked salmon dish"></div><div>Backed Salmon</div><div style="color:var(--muted)">⏱ 20min</div></div>
  </div>
  <nav class="nav"><span>Restaurant</span><span class="hub">Recipe</span><span>Meal Plan</span><span>Community</span><span>Menu</span></nav>
</div></div>

<!-- 20 Shop Ingredient -->
<div class="phone" style="left:317px;top:892px;height:185px"><div class="scr grey">
  <div class="sb"><span>5:50 am</span><i></i></div>
  <div class="hdr"><span class="avatar"></span><div><b>Hello Mira</b><small>Linden Square, Northvale</small></div><div class="tools"><span></span><span></span></div></div>
  <div class="title">Shop Ingredient</div>
  <div class="btn green pill" style="margin:1px 3px;justify-content:flex-start;padding-left:3px">⊕ Add Your Own Ingredient</div>
  <div class="list-item">● <div>Eggs<div style="font-size:1.6px;color:var(--muted)">as needed</div></div></div>
  <div class="list-item">● <div>Lemon<div style="font-size:1.6px;color:var(--muted)">as needed</div></div></div>
  <div class="list-item">● <div>Tomato<div style="font-size:1.6px;color:var(--muted)">2 piece</div></div></div>
  <div class="list-item">● <div>Tomato<div style="font-size:1.6px;color:var(--muted)">2 piece</div></div></div>
  <div class="list-item">● <div>Cardamom<div style="font-size:1.6px;color:var(--muted)">2 piece</div></div></div>
  <nav class="nav"><span>Restaurant</span><span class="hub">Recipe</span><span>Meal Plan</span><span>Community</span><span>Menu</span></nav>
</div></div>

<!-- 21 Meal Plan -->
<div class="phone" style="left:411px;top:892px;height:187px"><div class="scr grey">
  <div class="sb"><span>5:50 am</span><i></i></div>
  <div class="hdr"><span class="avatar"></span><div><b>Hello Mira</b><small>Linden Square, Northvale</small></div><div class="tools"><span></span><span></span></div></div>
  <div class="title">Meal Plan</div>
  <div class="card"><div class="p" style="text-align:center">Ready to plan this week</div>
    <div class="days"><span>16</span><span>17</span><span>18</span><span class="on">19</span><span>20</span><span>21</span><span>22</span></div></div>
  <div class="sub-banner" style="margin:1.5px 3px">Subscribe to<br><span style="font-weight:400;color:var(--muted)">Add your allergies or diet preferences</span></div>
  <div class="list-item"><span class="thumb img warm" role="img" aria-label="Scrambled eggs plate"></span><div><span style="font-size:1.5px;color:var(--muted)">Morning</span><br>Scrambled Eggs with Spinach, Feta &amp; Pita</div></div>
  <div class="list-item"><span class="thumb img" role="img" aria-label="Black bean salad"></span><div><span style="font-size:1.5px;color:var(--muted)">Afternoon</span><br>No-Cook Black Bean Salad</div></div>
  <div class="list-item"><span class="thumb img warm" role="img" aria-label="Glazed salmon with spinach"></span><div><span style="font-size:1.5px;color:var(--muted)">Evening</span><br>Gochujang-Glazed Salmon with Garlic Spinach</div></div>
  <nav class="nav"><span>Restaurant</span><span class="hub">Recipe</span><span>Meal Plan</span><span>Community</span><span>Menu</span></nav>
</div></div>

<!-- 22 Meal Plan – Subscription -->
<div class="phone" style="left:508px;top:925px;height:186px"><div class="scr grey">
  <div class="sb"><span>5:50 am</span><i></i></div>
  <div class="hdr"><span class="avatar"></span><div><b>Hello Mira</b><small>Linden Square, Northvale</small></div><div class="tools"><span></span><span></span></div></div>
  <div class="title">Meal Plan</div>
  <div class="card"><div class="p" style="text-align:center">Ready to plan this week</div>
    <div class="days"><span>16</span><span>17</span><span>18</span><span class="on">19</span><span>20</span><span>21</span><span>22</span></div></div>
  <div style="background:var(--green-soft);margin:1.5px 3px;padding:1.5px 2px;border-radius:1.5px;font-size:2px;font-weight:600">● Vegetarian <span class="chip fill" style="font-size:1.4px">Diet Plan</span><div style="font-weight:400;font-size:1.5px;color:var(--muted)">Excludes: Red Meat Poultry, Fish, Shellfish</div></div>
  <div class="list-item"><span class="thumb img warm" role="img" aria-label="Scrambled eggs plate"></span><div><span style="font-size:1.5px;color:var(--muted)">Morning · 450 kcl</span><br>Scrambled Eggs with Spinach, Feta &amp; Pita</div><span class="go"></span></div>
  <div class="list-item"><span class="thumb img" role="img" aria-label="Black bean salad"></span><div><span style="font-size:1.5px;color:var(--muted)">Afternoon · 380 kcl</span><br>No-Cook Black Bean Salad</div><span class="go"></span></div>
  <div class="list-item"><span class="thumb img warm" role="img" aria-label="Glazed salmon with spinach"></span><div><span style="font-size:1.5px;color:var(--muted)">Evening · 330 kcl</span><br>Gochujang-Glazed Salmon with Garlic Spinach</div><span class="go"></span></div>
  <nav class="nav"><span>Restaurant</span><span class="hub">Recipe</span><span>Meal Plan</span><span>Community</span><span>Menu</span></nav>
</div></div>

<svg width="18" height="30" style="position:absolute;left:586px;top:993px" viewBox="0 0 18 30"><path d="M0 4H16M13 2l3 2-3 2M0 26H16M13 24l3 2-3 2" stroke="#555" stroke-width=".6" fill="none"/></svg>
<div class="note" style="left:607px;top:995px">Premium user can add their diet plan</div>
<div class="note" style="left:607px;top:1017px">They can change their food also, using this edit icon</div>

<!-- Menu -->
<div class="phone" style="left:740px;top:912px;height:163px"><div class="scr grey">
  <div class="sb"><span>5:50 am</span><i></i></div>
  <div class="hdr"><span class="avatar"></span><div><b>Hello Mira</b><small>Linden Square, Northvale</small></div><div class="tools"><span></span><span></span></div></div>
  <div class="title">Menu</div>
  <div class="card" style="font-size:1.9px;line-height:2.9">
    <div>⌂ &nbsp;Meal Preparation</div><div>☰ &nbsp;Ingredient List</div><div>◯ &nbsp;Profile Info</div><div>? &nbsp;FAQ</div><div>↦ &nbsp;Logout</div>
  </div>
  <nav class="nav"><span>Restaurant</span><span class="hub">Recipe</span><span>Meal Plan</span><span>Community</span><span>Menu</span></nav>
</div></div>

<div class="thanks">Thanks for watching</div>
</body>
</html>
```